Powerpoint template for Marlow Brook Consulting

I need a powerpoint template for my business that would also work for Google slides.
I intermittently deliver training to people and I want a nice powerpoint template, that could also work in google docs to help make production easier and more seamless for me. I also sometimes product reports and analyses that are best done in powerpoint or Google slides. I need a title page, Title and content page, section heading page and any other pages that someone normally has!

Target Market(s)

Leaders and managers in medium to large companies. I provide training and coaching services to senior staff who have got 'stuck' and want help to find their way forward.

Font styles to use
Sans Serif

Requirements
Must have
• Colours and fonts to fit with logo please.
• Must include the logo and company name.
Nice to have
• a picture for the front?

```html
<!DOCTYPE html>
<html lang="en">
<head>
<meta charset="utf-8">
<title>Marlow Brook Consulting – Closing Slides</title>
<link rel="stylesheet" href="https://fonts.googleapis.com/css2?family=Open+Sans:wght@400;600;700&display=swap">
<style>
  :root {
    --canvas: #000000;
    --teal: #0bac8f;
    --teal-soft: #2bbd9f;
    --purple: #452f8f;
    --purple-soft: #573fa0;
    --violet: #4a4bd0;
    --violet-deep: #3f40bd;
    --white: #ffffff;
    --font-main: "Open Sans", Arial, sans-serif;
  }
  * { margin: 0; padding: 0; box-sizing: border-box; }
  html, body {
    width: 1095px;
    height: 1200px;
    overflow: hidden;
    background: var(--canvas);
    font-family: var(--font-main);
  }
  .canvas { position: relative; width: 1095px; height: 1200px; }

  .slide {
    position: absolute;
    left: 26px;
    width: 1042px;
    overflow: hidden;
  }
  .slide--thanks { top: 21px; height: 564px; background: var(--teal); }
  .slide--contact { top: 605px; height: 565px; background: var(--purple); }

  .backdrop-motif {
    position: absolute;
    left: 60px;
    top: 0;
    width: 560px;
    height: 100%;
  }
  .slide--thanks .backdrop-motif {
    background: radial-gradient(ellipse at 45% 45%, var(--teal-soft) 0%, rgba(11,172,143,0) 65%);
  }
  .slide--contact .backdrop-motif {
    background: radial-gradient(ellipse at 40% 40%, var(--purple-soft) 0%, rgba(69,47,143,0) 65%);
  }

  .guide-line {
    position: absolute;
    left: 69px;
    top: 0;
    width: 2px;
    background: var(--white);
  }
  .slide--thanks .guide-line { height: 376px; }
  .slide--contact .guide-line { height: 378px; }

  .accent-bar {
    position: absolute;
    left: 66px;
    width: 7px;
    border-radius: 3px;
  }
  .slide--thanks .accent-bar { top: 231px; height: 90px; background: var(--violet); }
  .slide--contact .accent-bar { top: 93px; height: 90px; background: var(--white); }

  .thanks-heading {
    position: absolute;
    left: 94px;
    top: 218px;
    color: var(--white);
    font-weight: 700;
    font-size: 44px;
    letter-spacing: 0.6px;
    line-height: 1.2;
    white-space: nowrap;
  }
  .thanks-subline {
    position: absolute;
    left: 97px;
    top: 278px;
    color: var(--white);
    font-weight: 400;
    font-size: 36px;
    line-height: 1.2;
    white-space: nowrap;
  }

  .award-badge {
    position: absolute;
    left: 667px;
    top: 81px;
    width: 328px;
    height: 442px;
    border-radius: 164px 164px 24px 24px;
    background: radial-gradient(ellipse at 50% 35%, var(--violet) 0%, var(--violet) 55%, var(--violet-deep) 100%);
  }

  .contact-heading {
    position: absolute;
    left: 98px;
    top: 106px;
    color: var(--white);
    font-weight: 700;
    font-size: 45px;
    line-height: 1.2;
    white-space: nowrap;
  }
  .contact-list {
    position: absolute;
    left: 103px;
    top: 202px;
    color: var(--white);
    font-size: 27px;
    line-height: 39px;
    list-style: none;
    white-space: nowrap;
  }
  .contact-list li + li { margin-top: 27px; }
  .contact-list .label { display: block; }

  .brand-panel {
    position: absolute;
    left: 708px;
    top: 0;
    width: 282px;
    height: 100%;
    background: var(--white);
    display: flex;
    flex-direction: column;
    align-items: center;
    justify-content: center;
    gap: 22px;
  }
  .brand-dot {
    width: 70px;
    height: 70px;
    border-radius: 50%;
    background: var(--teal);
  }
  .brand-name {
    color: var(--purple);
    font-family: var(--font-main);
    font-weight: 400;
    font-size: 30px;
    line-height: 1.2;
    text-align: center;
  }
</style>
</head>
<body>
<main class="canvas">

  <section class="slide slide--thanks">
    <div class="backdrop-motif" role="img" aria-label="Faint decorative brand motif in the background"></div>
    <span class="guide-line"></span>
    <span class="accent-bar"></span>
    <h1 class="thanks-heading">THANKS YOU SO MUCH</h1>
    <p class="thanks-subline">For your valuable times</p>
    <div class="award-badge" role="img" aria-label="Thank you award rosette with ribbons"></div>
  </section>

  <section class="slide slide--contact">
    <div class="backdrop-motif" role="img" aria-label="Faint decorative brand motif in the background"></div>
    <span class="guide-line"></span>
    <span class="accent-bar"></span>
    <h2 class="contact-heading">Contact Me</h2>
    <ul class="contact-list">
      <li><span class="label">Email Id :</span>hello@marlowbrookconsulting.com</li>
      <li><span class="label">Website :</span>www.marlowbrookconsulting.com</li>
    </ul>
    <div class="brand-panel">
      <span class="brand-dot"></span>
      <p class="brand-name">MARLOW BROOK<br>CONSULTING</p>
    </div>
  </section>

</main>
</body>
</html>
```